Personal Training Business at home (Fern Wellness & Health)

My business name will be Fern Wellness & Health and will be training people with special needs (Asthma, Diabetes, Obesity, Rehab, Sports Performance) for all ages. It will be set indoor and outdoor for all types of weather conditions. I,m also doing Pilates group classes as well in a Japanese garden setting.I will be working alone so the groups will be small and the client has a high quality of service. I just need something very basic to start with then as the business expands I can edit it to it,s growth.

Target Market(s)

Target special population persons with dysfunctions injuries, metabolic/cardio-respiratory conditions, sports performance and more also healthy food choices.

Industry/Entity Type

Business

Number of Pages Required

3 page

Font styles to use
Serif

Colors
f78f20
ffffff
474747
cbcbcb
abd036

Requirements
Must have
• The website must have accessibility for change, to be able to link on other networks like my own (omitted) videos. A basic lay out so I can fill in the pages and ad more as I expand the business. The logo to have the A for Arch to be an image of a man shaped as the letter A with his arms extended out/up. Private Facility and must ring for appointment to enter premises.
Nice to have
• The Image I want to have in my studio is for people to be serious about training & health choices. I want them to be able to train in a comfortable environment and free of air conditioned concrete rooms with machines. My home is converted to a Organic feature and outdoor/indoor training facility that my clients & I can share the natural freedom of training in the elements. My client have special needs and need extra care, they are people with injuries, metabolic/cardio-respiratory condition, asthmatics & more they need to be screened and tested for the condition that they suffer from and together with there allied professional we work together to treat them with the up most care for maximum results. This is what I want to target I long term client with real Goals on there mind and not some pipe dream.
Should not have
• Not to be portray as a Gym with machines and clients that only care about image.

```html
<!DOCTYPE html>
<html lang="en">
<head>
<meta charset="utf-8">
<title>Fern Wellness &amp; Health</title>
<link rel="stylesheet" href="https://fonts.googleapis.com/css2?family=Roboto:wght@300;400;500;700&display=swap">
<style>
:root{
  --green:#abd036;
  --orange:#f78f20;
  --dark:#474747;
  --darker:#353535;
  --light:#cbcbcb;
  --pale:#efefef;
  --white:#ffffff;
  --text:#6a6a6a;
}
*{margin:0;padding:0;box-sizing:border-box}
html,body{width:1200px;height:3030px;overflow:hidden}
body{position:relative;font-family:'Roboto',Arial,sans-serif;background:var(--white);color:var(--dark)}
.abs{position:absolute}

/* hero */
.hero{left:0;top:0;width:1200px;height:592px;background:linear-gradient(180deg,#4b463e 0%,#5d5348 45%,#6e5f55 75%,#5a4c44 100%)}
.hero-shade{left:0;top:0;width:1200px;height:592px;background:rgba(30,25,30,.35)}
.topbar{left:0;top:0;width:1200px;height:44px;background:rgba(40,40,40,.75);color:#cfcfcf;font-size:12px}
.topbar .contact{left:99px;top:15px;display:flex;gap:28px}
.topbar .contact span{display:flex;align-items:center;gap:7px}
.topbar .tools{right:101px;top:15px;display:flex;gap:16px;align-items:center}
.dot{width:8px;height:8px;border-radius:50%;background:var(--orange);display:inline-block}
.brand{left:101px;top:104px;display:flex;align-items:center;gap:12px}
.brand-mark{width:30px;height:30px;border-radius:50%;background:var(--orange)}
.brand-name{font-size:30px;font-weight:700;color:var(--white);letter-spacing:.5px}
.nav{right:98px;top:89px;display:flex;gap:42px;font-size:12px;font-weight:700;color:var(--white)}
.nav .active{color:var(--green)}
.slide-arrow{top:292px;width:52px;height:52px;border-radius:50%;background:rgba(120,120,120,.6)}
.slide-arrow.left{left:45px}.slide-arrow.right{right:45px}
.hero-title{left:0;width:1200px;top:385px;text-align:center;font-size:52px;font-weight:500;color:var(--white)}
.hero-sub{left:0;width:1200px;top:444px;text-align:center;font-size:19px;font-weight:300;color:var(--white);letter-spacing:.3px}
.view-more{left:0;width:1200px;top:526px;text-align:center;font-size:18px;font-weight:500;color:var(--white)}

/* welcome */
.welcome-title{left:0;width:1200px;top:697px;text-align:center;font-size:24px;font-weight:500;color:#333}
.welcome-text{left:140px;width:920px;top:742px;text-align:center;font-size:11px;line-height:20px;color:#777}
.btn{left:545px;top:848px;width:108px;height:41px;background:var(--orange);color:var(--white);font-size:11px;font-weight:500;display:flex;align-items:center;justify-content:center;border-radius:2px}

/* services */
.services{left:0;top:925px;width:1200px;height:461px;background:var(--pale)}
.section-title{left:0;width:1200px;top:961px;text-align:center;font-size:24px;font-weight:500;color:#333}
.card{top:1032px;width:238px;height:295px;overflow:hidden}
.card-photo{width:100%;height:100%}
.card-caption{left:0;bottom:0;width:100%;height:105px;background:rgba(40,40,40,.55);color:var(--white);text-align:center;padding-top:12px}
.card-caption h3{font-size:18px;font-weight:500;margin-bottom:5px}
.card-caption p{font-size:11px;line-height:15px;padding:0 18px;color:#e6e6e6}
.carousel-edge{top:1090px;width:20px;height:70px}

/* video */
.video{left:99px;top:1426px;width:1002px;height:564px;background:linear-gradient(180deg,#2a2d25 0%,#3a3026 50%,#5e4634 100%)}
.play{left:553px;top:1652px;width:90px;height:60px;background:rgba(20,20,20,.85);border-radius:12px;border:1px solid #555}
.player-bar{left:99px;top:1929px;width:1002px;height:61px;background:#1c1c1c}
.progress{left:99px;top:1929px;width:1002px;height:6px;background:#d41c1c}
.time{left:287px;top:1952px;font-size:20px;color:var(--white)}

/* special */
.special{left:0;top:2036px;width:1200px;height:580px;background:linear-gradient(100deg,#2a2c22 0%,#3c3d2d 50%,#4d4a36 100%)}
.special-title{left:99px;top:2090px;font-size:24px;font-weight:500;color:var(--white)}
.tile{width:303px;border:3px solid var(--white);overflow:hidden}
.tile-photo{width:100%;height:100%}
.tile-label{left:22px;bottom:22px;width:256px;height:42px;background:rgba(40,40,40,.75);color:var(--white);font-size:16px;font-weight:500;display:flex;align-items:center;justify-content:space-between;padding:0 12px 0 18px}
.plus{width:24px;height:24px;border-radius:50%;border:2px solid var(--orange);color:var(--orange);font-size:18px;line-height:19px;text-align:center}
.hours{left:747px;top:2157px;width:354px;height:408px;background:rgba(140,135,60,.55);color:var(--white)}
.hours h3{font-size:24px;font-weight:500;padding:32px 12px 20px}
.season{height:34px;background:rgba(170,140,40,.6);font-size:16px;font-weight:500;padding:8px 12px}
.hours table{width:100%;border-collapse:collapse;font-size:12px;margin:8px 0 26px}
.hours td{padding:8px 0 8px 12px}
.hours td.day{font-weight:700;width:118px}

/* connect + footer */
.footer{left:0;top:2814px;width:1200px;height:216px;background:var(--dark)}
.social{top:2662px;width:38px;height:38px;border-radius:50%;border:2px solid var(--white)}
.connect{left:0;width:1200px;top:2733px;text-align:center;font-size:15px;font-weight:500;color:var(--white)}
.footer-brand{left:0;width:1200px;top:2932px;display:flex;justify-content:center;align-items:center;gap:12px}
.footer-brand .brand-name{font-size:32px}
.copyright{left:0;width:1200px;top:2990px;text-align:center;font-size:12px;color:#ddd}
</style>
</head>
<body>

<section class="abs hero" role="img" aria-label="Japanese garden with bonsai trees and pebble beds"></section>
<div class="abs hero-shade"></div>

<header>
  <div class="abs topbar">
    <div class="abs contact">
      <span><i class="dot"></i>(1) 555 010 42731</span>
      <span><i class="dot"></i>info@fernwellness.com</span>
    </div>
    <div class="abs tools">
      <span>Language</span><i class="dot"></i><i class="dot"></i>
      <svg width="12" height="12" viewBox="0 0 12 12"><circle cx="5" cy="5" r="3.5" fill="none" stroke="#f78f20" stroke-width="1.6"/><line x1="7.5" y1="7.5" x2="11" y2="11" stroke="#f78f20" stroke-width="1.6"/></svg>
    </div>
  </div>
  <div class="abs brand"><span class="brand-mark"></span><span class="brand-name">FERN WELLNESS</span></div>
  <nav class="abs nav"><span class="active">HOME</span><span>ABOUT</span><span>TRAINING</span><span>NEWS</span><span>CONTACT</span></nav>
</header>

<div class="abs slide-arrow left"><svg width="52" height="52"><polyline points="30,16 20,26 30,36" fill="none" stroke="#222" stroke-width="4"/></svg></div>
<div class="abs slide-arrow right"><svg width="52" height="52"><polyline points="22,16 32,26 22,36" fill="none" stroke="#222" stroke-width="4"/></svg></div>

<h1 class="abs hero-title">PILATES GROUP CLASSES</h1>
<p class="abs hero-sub">FERNWELL HAS TRAINERS THAT HAVE A DIPLOMA OF FITNESS FROM THE LINDEN INSTITUTE</p>

<svg class="abs" style="left:0;top:491px" width="1200" height="190">
  <polygon points="470,0 760,0 615,185" fill="#e6e6e6"/>
  <polygon points="485,0 717,0 601,161" fill="#abd036"/>
  <polyline points="591,80 601,90 611,80" fill="none" stroke="#474747" stroke-width="5"/>
</svg>
<div class="abs view-more">VIEW MORE</div>

<section>
  <h2 class="abs welcome-title">WELCOME TO FERN WELLNESS</h2>
  <p class="abs welcome-text">FERNWELL has trainers that have a Diploma of fitness from the Linden Institute &amp; are trained and qualified with the latest training techniques available anywhere in Australia, to give clients a better &amp; more reliable service with cutting edge training programs and testing. The foundation of this business will be to service clients by functional training techniques and some machines, with a combination of group classes &amp; one on one personal training. We also have an area for Pilates experience, this is a very Japanese influenced setting &amp; is called Organic Pilates experience.</p>
  <div class="abs btn">READ MORE</div>
</section>

<section>
  <div class="abs services"></div>
  <h2 class="abs section-title">TRAINING SERVICES</h2>
  <svg class="abs carousel-edge" style="left:62px"><polyline points="16,2 4,35 16,68" fill="none" stroke="#cbcbcb" stroke-width="2"/></svg>
  <svg class="abs carousel-edge" style="left:1118px"><polyline points="4,2 16,35 4,68" fill="none" stroke="#cbcbcb" stroke-width="2"/></svg>

  <article class="abs card" style="left:99px">
    <div class="card-photo" role="img" aria-label="Trainer stretching a client's leg outdoors" style="background:linear-gradient(160deg,#6f9a3a,#3e6a24 60%,#8aa36a)"></div>
    <div class="abs card-caption"><h3>PERSONAL TRAINING</h3><p>Our training services covers a wide variety of clients from different walks of life, like builders.</p></div>
  </article>
  <article class="abs card" style="left:354px">
    <div class="card-photo" role="img" aria-label="Group exercising with fitness balls on grass" style="background:linear-gradient(160deg,#3f7a3a,#5c8e4a 50%,#4a7fb0)"></div>
    <div class="abs card-caption"><h3>GROUP FUNCTIONAL</h3><p>Our training services covers a wide variety of clients from different walks of life, like builders.</p></div>
  </article>
  <article class="abs card" style="left:608px">
    <div class="card-photo" role="img" aria-label="Woman meditating in a green park" style="background:linear-gradient(160deg,#4f9a35,#82b84c 55%,#d9cfc0)"></div>
    <div class="abs card-caption"><h3>PILATES</h3><p>Our training services covers a wide variety of clients from different walks of life, like builders.</p></div>
  </article>
  <article class="abs card" style="left:863px">
    <div class="card-photo" role="img" aria-label="Runner silhouetted against a sunset" style="background:linear-gradient(170deg,#c7641b,#f0a030 45%,#6a2e10)"></div>
    <div class="abs card-caption"><h3>SPORTS PERFORMANCE</h3><p>Our training services covers a wide variety of clients from different walks of life, like builders.</p></div>
  </article>
</section>

<section>
  <div class="abs video" role="img" aria-label="Video still of a wooden deck in the training garden"></div>
  <div class="abs play"><svg width="90" height="60"><polygon points="37,18 37,42 58,30" fill="#fff"/></svg></div>
  <div class="abs player-bar"></div>
  <div class="abs progress"></div>
  <svg class="abs" style="left:99px;top:1923px" width="1002" height="67">
    <circle cx="16" cy="9" r="9" fill="#ddd"/>
    <polygon points="40,30 40,52 58,41" fill="#ccc"/>
    <rect x="116" y="35" width="7" height="12" fill="#ccc"/><polygon points="123,35 134,27 134,55 123,47" fill="#ccc"/>
    <circle cx="814" cy="41" r="8" fill="#ccc"/>
    <path d="M948 32h-6v6M968 32h6v6M948 52h-6v-6M968 52h6v-6" fill="none" stroke="#ccc" stroke-width="3"/>
  </svg>
  <div class="abs time">0:00 / 3:00</div>
</section>

<section>
  <div class="abs special" role="img" aria-label="Blurred outdoor path with a runner at dusk"></div>
  <h2 class="abs special-title">OUR SPECIAL TRAINING WITH</h2>

  <div class="abs tile" style="left:99px;top:2161px;height:199px">
    <div class="tile-photo" role="img" aria-label="Woman using an asthma inhaler" style="background:linear-gradient(150deg,#e9e4e1,#c9a8a0 60%,#a0626a)"></div>
    <div class="abs tile-label">ASTHMA<span class="plus">+</span></div>
  </div>
  <div class="abs tile" style="left:416px;top:2161px;height:199px">
    <div class="tile-photo" role="img" aria-label="Blood glucose meter being used" style="background:linear-gradient(150deg,#d9dde2,#8d9096 55%,#4a4c50)"></div>
    <div class="abs tile-label">DIABETES<span class="plus">+</span></div>
  </div>
  <div class="abs tile" style="left:99px;top:2372px;height:191px">
    <div class="tile-photo" role="img" aria-label="Close view of a waistline in tight jeans" style="background:linear-gradient(120deg,#1a1a1a,#3a3632 50%,#b7aa95)"></div>
    <div class="abs tile-label">OBESITY<span class="plus">+</span></div>
  </div>
  <div class="abs tile" style="left:416px;top:2372px;height:191px">
    <div class="tile-photo" role="img" aria-label="Runner's legs on a sunlit trail" style="background:linear-gradient(150deg,#f0a860,#c56a3a 55%,#6a4a3a)"></div>
    <div class="abs tile-label">SPORTS<span class="plus">+</span></div>
  </div>

  <aside class="abs hours">
    <h3>TRADING HOURS</h3>
    <div class="season">APRIL - SEPTEMBER</div>
    <table>
      <tr><td class="day">Monday – Friday</td><td>4.00pm - 6.00pm (Finish by 7.00pm)</td></tr>
      <tr><td class="day">Saturday-</td><td>12.00pm – 5-00pm (Finish by 6.00pm)</td></tr>
      <tr><td class="day">Sunday -</td><td>6.00am – 11.00am (Finish by 12.00pm)</td></tr>
    </table>
    <div class="season">OCTOBER – MARCH</div>
    <table>
      <tr><td class="day">Monday – Friday</td><td>6.00am – 7.00pm (Finish by 8.00pm)</td></tr>
      <tr><td class="day">Saturday-</td><td>12.00pm – 5-00pm (Finish by 6.00pm)</td></tr>
      <tr><td class="day">Sunday -</td><td>6.00am – 11.00am (Finish by 12.00pm)</td></tr>
    </table>
  </aside>
</section>

<footer>
  <div class="abs footer"></div>
  <svg class="abs" style="left:0;top:2616px" width="1200" height="300">
    <polygon points="283,0 919,0 601,260" fill="#e3e3e3"/>
    <polygon points="330,0 872,0 601,230" fill="#abd036"/>
    <polyline points="590,198 601,188 612,198" fill="none" stroke="#474747" stroke-width="5"/>
  </svg>
  <div class="abs social" style="left:454px"></div>
  <div class="abs social" style="left:516px"></div>
  <div class="abs social" style="left:579px"></div>
  <div class="abs social" style="left:642px"></div>
  <div class="abs social" style="left:706px"></div>
  <div class="abs connect">CONNECT WITH US</div>
  <div class="abs footer-brand"><span class="brand-mark"></span><span class="brand-name">FERN WELLNESS</span></div>
  <p class="abs copyright">@ Copy Rights -2016 fernwellness.com - all rights reserved</p>
</footer>

</body>
</html>
```